Junk Removal business needs a small billboard design

We are looking to have a billboard design made that will pop out to motorist passing by. The sign will be 6 foot wide by 4 foot tall. We would like it to say:SHOW US YOUR JUNK! 614-285-3907 BIG OR SMALL... WE HAUL IT ALL VICTORY JUNK REMOVALWe have provided a rough draft sketch photo of how large we would want the text. Preferably we want the text to be very large and use up most of the space and to be seen from far away. Also, there are example photos of the green background color and text colors we would like to incorporate into the design. We would like to add our company logo (Files attached) on the billboard too. Next to the phone number we would like to add the camera icon (example photos attached) Thank you in advance for all your hard work!

Font styles to use
Serif
Sans Serif

Requirements
Must have
• Large font that is easy to read from far
• Company name must be large
Nice to have
• Bright and pop out to passing by motorist.

```html
<!DOCTYPE html>
<html lang="en">
<head>
<meta charset="utf-8">
<title>Marlowe Junk Removal – Billboard</title>
<link rel="stylesheet" href="https://fonts.googleapis.com/css2?family=Montserrat:wght@700;800;900&display=swap">
<style>
  :root {
    --backdrop: #d9d9d9;
    --board: #ffffff;
    --ink: #0d0d0d;
    --orange: #f05a30;
    --camera-brown: #c8582c;
    --camera-top: #e9e2d4;
    --slate: #4a4a4a;
    --white: #ffffff;
  }
  html, body {
    margin: 0;
    padding: 0;
    width: 1200px;
    height: 1000px;
    overflow: hidden;
    background: var(--backdrop);
  }
  .billboard {
    position: absolute;
    left: 78px;
    top: 152px;
    width: 1044px;
    height: 696px;
    background: var(--board);
  }
  .billboard svg {
    display: block;
    font-family: 'Montserrat', Arial, sans-serif;
  }
  .headline-small { font-weight: 800; fill: var(--ink); }
  .headline-junk {
    font-weight: 900;
    fill: var(--orange);
    stroke: var(--ink);
    stroke-width: 9;
    paint-order: stroke fill;
    stroke-linejoin: round;
  }
  .phone-number { font-weight: 800; fill: var(--ink); }
  .ribbon { fill: var(--orange); }
  .ribbon-text { font-weight: 800; fill: var(--white); }
  .footer-band { fill: var(--ink); }
  .footer-rule { fill: var(--orange); }
  .logo-panel { fill: var(--slate); }
  .company-name { font-weight: 800; fill: var(--white); }
  .brand-mark-text { font-weight: 800; fill: var(--white); }
  .brand-dot { fill: var(--orange); }
  .camera-body { fill: var(--camera-brown); stroke: var(--ink); stroke-width: 4; }
  .camera-top { fill: var(--camera-top); stroke: var(--ink); stroke-width: 4; }
  .camera-lens-ring { fill: var(--camera-top); stroke: var(--ink); stroke-width: 4; }
  .camera-lens { fill: #555; stroke: var(--ink); stroke-width: 3; }
</style>
</head>
<body>
  <main class="billboard">
    <svg width="1044" height="696" viewBox="0 0 1044 696" xmlns="http://www.w3.org/2000/svg">
      <text class="headline-small" x="159" y="96" font-size="86" textLength="726" lengthAdjust="spacingAndGlyphs">SHOW US YOUR</text>
      <text class="headline-junk" x="42" y="324" font-size="292" textLength="963" lengthAdjust="spacingAndGlyphs">JUNK !</text>

      <g class="camera-icon" aria-label="Camera icon">
        <rect class="camera-body" x="132" y="364" width="98" height="62" rx="10"/>
        <path class="camera-top" d="M134 392 v-18 a10 10 0 0 1 10 -10 h22 l8 -12 h28 l8 12 h10 a10 10 0 0 1 10 10 v18 z"/>
        <circle class="camera-lens-ring" cx="180" cy="392" r="26"/>
        <circle class="camera-lens" cx="180" cy="392" r="16"/>
      </g>
      <text class="phone-number" x="257" y="424" font-size="96" textLength="665" lengthAdjust="spacingAndGlyphs">614-285-3907</text>

      <polygon class="ribbon" points="72,451 992,451 970,483.5 992,516 72,516 94,483.5"/>
      <text class="ribbon-text" x="92" y="502" font-size="50" textLength="870" lengthAdjust="spacingAndGlyphs">BIG OR SMALL...WE HAUL IT ALL</text>

      <rect class="footer-rule" x="250" y="600" width="794" height="7"/>
      <rect class="footer-band" x="250" y="607" width="794" height="89"/>
      <polygon class="logo-panel" points="0,531 222,531 327,696 0,696"/>

      <g class="brand-mark">
        <circle class="brand-dot" cx="40" cy="612" r="14"/>
        <text class="brand-mark-text" x="64" y="604" font-size="26">MARLOWE</text>
        <text class="brand-mark-text" x="64" y="634" font-size="18">JUNK REMOVAL</text>
      </g>

      <text class="company-name" x="324" y="672" font-size="50" textLength="666" lengthAdjust="spacingAndGlyphs">MARLOWE JUNK REMOVAL</text>
    </svg>
  </main>
</body>
</html>
```